Plumbing business card and logo desgin

Need a new business card and logo for a plumbing business based in Warragul, Australia. Business name is 7Kelby plumbing & air-conditioning. We service all plumbing and gasfitting needs and installation of air-conditioning. We clear blocked drains, install new hot water systems, central heating, new and existing homes, roofing, sanitary and drainage.
i would like to have a space on there for website, email, phone, licence number and what we do as a company.
i would like a water droplet to be incorporated into the design to try and stand out that we are a plumbing business

Contact Information for Business Card

website:
phone number: 0458271936
Licence Number: 382716

Logo Text

7Kelby Plumbing & Air-Conditioning

```html
<!DOCTYPE html>
<html lang="en">
<head>
<meta charset="utf-8">
<title>7Kelby Plumbing &amp; Air-Conditioning – Business Card</title>
<link rel="stylesheet" href="https://fonts.googleapis.com/css2?family=Poppins:wght@400;500;600&display=swap">
<style>
  :root {
    --stage: #d9d4cc;
    --navy-deep: #0b0a3c;
    --navy: #25235e;
    --frost-light: #f1f2f4;
    --frost-mid: #d7dade;
    --teal: #2aa3b8;
    --silver: #c9c6cf;
    --text-main: #f4f3f8;
    --text-soft: #dcdbe8;
    --text-licence: #e9d6dc;
    --brand: #1a1850;
  }
  * { box-sizing: border-box; margin: 0; padding: 0; }
  html, body { width: 1200px; height: 970px; overflow: hidden; }
  body { background: var(--stage); font-family: "Poppins", sans-serif; position: relative; }

  .business-card {
    position: absolute; left: 80px; top: 190px;
    width: 1040px; height: 590px;
    border-radius: 24px; overflow: hidden;
    box-shadow: 0 18px 40px rgba(0,0,0,0.18);
  }
  .card-shapes { position: absolute; inset: 0; }

  .contact-panel { position: absolute; left: 60px; top: 0; color: var(--text-main); }
  .person-name { position: absolute; top: 104px; font-size: 37px; font-weight: 500; white-space: nowrap; letter-spacing: 0.3px; }
  .person-role { position: absolute; top: 150px; font-size: 25px; font-weight: 400; color: var(--text-soft); }
  .name-rule { position: absolute; top: 228px; width: 112px; height: 3px; background: var(--text-main); }

  .contact-list { position: absolute; top: 290px; list-style: none; }
  .contact-item { display: flex; align-items: center; height: 38px; font-size: 26px; color: var(--text-soft); white-space: nowrap; }
  .contact-icon { width: 22px; height: 22px; margin-right: 16px; flex: none; }
  .licence { position: absolute; top: 436px; font-size: 25px; color: var(--text-licence); white-space: nowrap; }

  .brand-mark {
    position: absolute; left: 620px; top: 225px; width: 320px;
    text-align: center; color: var(--brand);
    font-weight: 600; font-size: 28px; line-height: 1.3;
  }
</style>
</head>
<body>
  <section class="business-card" aria-label="7Kelby Plumbing &amp; Air-Conditioning business card">
    <svg class="card-shapes" viewBox="0 0 1040 590" preserveAspectRatio="none" aria-hidden="true">
      <defs>
        <linearGradient id="frost" x1="0" y1="0" x2="1" y2="1">
          <stop offset="0" stop-color="var(--frost-light)"/>
          <stop offset="1" stop-color="var(--frost-mid)"/>
        </linearGradient>
        <radialGradient id="navyGlow" cx="0.45" cy="0.45" r="0.7">
          <stop offset="0" stop-color="var(--navy)"/>
          <stop offset="0.6" stop-color="var(--navy-deep)"/>
          <stop offset="1" stop-color="var(--navy)"/>
        </radialGradient>
      </defs>
      <rect width="1040" height="590" fill="url(#frost)"/>
      <path d="M0 0 H562 C470 170 470 420 560 590 H0 Z" fill="url(#navyGlow)"/>
      <path d="M562 0 C470 170 470 420 560 590" fill="none" stroke="var(--silver)" stroke-width="10"/>
      <path d="M568 0 C482 170 482 420 566 590" fill="none" stroke="var(--teal)" stroke-width="4"/>
    </svg>

    <div class="contact-panel">
      <h1 class="person-name">Liam Carter</h1>
      <p class="person-role">Director</p>
      <div class="name-rule"></div>

      <ul class="contact-list">
        <li class="contact-item">
          <svg class="contact-icon" viewBox="0 0 24 24"><path d="M6 2l4 4-2 3c1 3 4 6 7 7l3-2 4 4-3 4C10 21 3 14 2 5z" fill="none" stroke="currentColor" stroke-width="1.8"/></svg>
          0458271936
        </li>
        <li class="contact-item">
          <svg class="contact-icon" viewBox="0 0 24 24"><rect x="2" y="5" width="20" height="14" fill="currentColor"/><path d="M2 5l10 8 10-8" fill="none" stroke="var(--navy-deep)" stroke-width="1.6"/></svg>
          info@7kelbymail.com
        </li>
        <li class="contact-item">
          <svg class="contact-icon" viewBox="0 0 24 24" fill="none" stroke="currentColor" stroke-width="1.5"><circle cx="12" cy="12" r="10"/><ellipse cx="12" cy="12" rx="4.5" ry="10"/><path d="M2 12h20M4 7h16M4 17h16"/></svg>
          www.7kelbyweb.com
        </li>
      </ul>

      <p class="licence">Licence Number: 382716</p>
    </div>

    <p class="brand-mark">7Kelby<br>Plumbing &amp;<br>Air-Conditioning</p>
  </section>
</body>
</html>
```